Branding Pack for new business to business cost saving site

I would like a branding pack for my new project. I would like the following designed;
a4 Presentation folder
Letterhead
Envelope
Business Card
compliment splip

We are a business cost saving site, we have access to 1000s of discount offers for daily business to business offers. I already have the logo therfore please follow th e logo for the coloutr and design.

Target Market(s)

SMEs in United Kingdom

Industry/Entity Type

Business Service

Font styles to use
Serif
Script

Colors
0255a3
fbee3d

Requirements
Must have
• The folder needs to be the same size as attached

```html
<!DOCTYPE html>
<html lang="en">
<head>
<meta charset="utf-8">
<title>tallypal stationery set</title>
<link href="https://fonts.googleapis.com/css2?family=Montserrat:wght@400;500;700&family=Lato:wght@400;700&display=swap" rel="stylesheet">
<style>
  :root{
    --navy:#2e3877;
    --yellow:#fdd04a;
    --paper:#ffffff;
    --slip:#f4f4f4;
    --backdrop:#c2b49a;
    --ink:#333333;
    --shadow:0 2px 5px rgba(0,0,0,.18);
  }
  *{box-sizing:border-box;margin:0;padding:0}
  html,body{width:1200px;height:1200px;overflow:hidden}
  body{background:var(--backdrop);font-family:"Lato",sans-serif;color:var(--ink);position:relative}
  .piece{position:absolute;overflow:hidden;box-shadow:var(--shadow)}
  .brand{font-family:"Montserrat",sans-serif;font-weight:500;color:var(--navy);letter-spacing:-.01em;line-height:1;white-space:nowrap}
  .brand.light{color:#fff}
  .deco{position:absolute;inset:0;width:100%;height:100%}

  /* letterhead */
  .letterhead{left:138px;top:70px;width:355px;height:501px;background:var(--paper);border-top:5px solid var(--navy)}
  .letterhead .brand{position:absolute;left:52px;top:47px;font-size:18px}
  .letterhead .address{position:absolute;left:52px;top:74px;font-size:6.6px}
  .letterhead .contacts{position:absolute;left:258px;top:62px;font-size:3.6px;line-height:6.4px}
  .contacts li{list-style:none;display:flex;align-items:center;gap:3px}
  .dot{display:inline-block;width:4px;height:4px;border-radius:50%;background:var(--navy)}
  .recipient{position:absolute;left:52px;top:116px;font-size:5.6px;line-height:6px}
  .recipient strong{font-size:6px}
  .recipient small{display:block;font-size:3.4px}
  .date{position:absolute;left:255px;top:132px;font-size:5.8px;font-weight:700}
  .body-copy{position:absolute;left:52px;top:153px;width:252px;font-size:5.35px;line-height:7.2px;text-align:justify}
  .body-copy p{margin-bottom:7.2px}
  .signature{position:absolute;left:60px;top:396px;width:50px;height:14px;background:linear-gradient(90deg,#d9d9d9,#bdbdbd);border-radius:2px}
  .signer{position:absolute;left:54px;top:424px;font-size:7px;font-weight:700;letter-spacing:.04em}
  .signer small{display:block;font-size:5px;font-weight:400;letter-spacing:0;margin-top:2px}

  /* business cards */
  .card-front{left:463px;top:218px;width:150px;height:86px;background:var(--paper)}
  .card-front .brand{position:absolute;left:22px;top:31px;font-size:9.5px}
  .card-front .person{position:absolute;left:22px;top:45px;font-size:3.8px;color:var(--navy);font-weight:700;line-height:5px}
  .card-front .person span{font-weight:400;color:var(--ink);display:block}
  .card-front .rule{position:absolute;left:75px;top:28px;width:1px;height:34px;background:var(--navy)}
  .card-front .contacts{position:absolute;left:81px;top:30px;font-size:3px;line-height:5.8px}
  .card-front .dot{width:3.4px;height:3.4px}
  .card-back{left:463px;top:316px;width:150px;height:86px;background:var(--navy)}
  .card-back .brand{position:absolute;right:10px;top:66px;font-size:9px}

  /* envelopes */
  .envelope-back{left:662px;top:142px;width:371px;height:186px;background:var(--navy)}
  .envelope-back .flap{position:absolute;left:0;top:0;width:100%;height:61px;background:#f3f3f3;border-radius:0 0 10px 10px}
  .envelope-back .brand{position:absolute;left:130px;top:23px;font-size:22px}
  .envelope-front{left:664px;top:357px;width:371px;height:186px;background:var(--navy)}
  .envelope-front .brand{position:absolute;left:28px;top:31px;font-size:22px}
  .envelope-front .contacts{position:absolute;left:28px;top:124px;font-size:6.8px;line-height:9.4px;color:#fff}
  .envelope-front .window{position:absolute;left:222px;top:96px;width:124px;height:62px;border-radius:8px;background:linear-gradient(110deg,#fafafa 45%,#dcdcdc 55%,#f4f4f4 70%)}

  /* folder */
  .folder{position:absolute;left:86px;top:600px;width:744px;height:546px}
  .folder-flaps{position:absolute;left:0;top:0;width:744px;height:546px}
  .folder .cover-back{position:absolute;left:66px;top:0;width:338px;height:466px;background:var(--navy)}
  .folder .cover-front{position:absolute;left:404px;top:0;width:340px;height:466px;background:var(--paper);overflow:hidden}
  .cover-front .brand{position:absolute;left:91px;top:372px;font-size:36px}
  .folder-contacts{position:absolute;left:80px;top:438px;display:flex;gap:20px;font-size:3.6px;color:#fff;align-items:center}
  .folder-contacts span{display:flex;align-items:center;gap:4px}

  /* compliment slip */
  .slip{left:786px;top:804px;width:308px;height:146px;background:var(--slip)}
  .slip .brand{position:absolute;left:24px;top:26px;font-size:15px}
  .slip .contacts{position:absolute;left:25px;top:86px;font-size:5px;line-height:7px}
  .slip .ribbon{position:absolute;left:0;top:116px;width:150px;height:18px;background:var(--navy);clip-path:polygon(0 0,88% 0,100% 100%,0 100%);color:#fff;font-family:"Montserrat",sans-serif;font-weight:700;font-size:8.2px;padding:4px 0 0 26px}
</style>
</head>
<body>

<section class="piece letterhead">
  <div class="brand">tallypal</div>
  <div class="address">48 Orchard Rd. Halden, FL 32871</div>
  <ul class="contacts">
    <li><span class="dot"></span>00-987-654-321</li>
    <li><span class="dot"></span>hello@tallypal.com</li>
    <li><span class="dot"></span>www.tallypal.com</li>
  </ul>
  <div class="recipient"><strong>Dear, Mr________</strong><small>Designation</small><small><b>COMPANY NAME</b></small></div>
  <div class="date">DATE:1/5/2018</div>
  <div class="body-copy">
    <p>Lorem Ipsum is simply dummy text of the printing and typesetting industry. Lorem Ipsum has been the industry's standard dummy text ever since the1500s,when an unknown printer took a galley of type and scrambled it to make a type specimen book. It has survived not only five centuries, but also the leap into electronic typesetting, remaining essentially unchanged. It was popularised in the 1960s with the release of Letraset sheets containing Lorem Ipsum passages, and more recently with desktop publishing software like Aldus PageMaker including versions of Lorem Ipsum.</p>
    <p>Lorem Ipsum is simply dummy text of the printing and typesetting industry. Lorem Ipsum has been the industry's standard dummy text ever since the1500s,when an unknown printer took a galley of type and scrambled it to make a type specimen book. It has survived not only five centuries, but also the leap into electronic typesetting, remaining essentially unchanged. It was popularised in the 1960s with the release of Letraset sheets containing Lorem Ipsum passages, and more recently with desktop publishing software like Aldus PageMaker including versions of Lorem Ipsum.</p>
    <p>Lorem Ipsum is simply dummy text of the printing and typesetting industry. Lorem Ipsum has been the industry's standard dummy text ever since the1500s,when an unknown printer took a galley of type and scrambled it to make a type specimen book. It has survived not only five centuries, but also the leap into electronic typesetting, remaining essentially unchanged. It was popularised in the 1960s with the release of Letraset sheets containing Lorem Ipsum passages, and more recently with desktop publishing software like Aldus PageMaker including versions of Lorem Ipsum.</p>
    <p>Lorem Ipsum is simply dummy text of the printing and typesetting industry. Lorem Ipsum has been the industry's standard dummy text ever since the1500s,when an unknown printer took a galley of type and scrambled it to make a type specimen book. It has survived not only five centuries, but also the leap into electronic typesetting, remaining essentially unchanged. It was popularised in the 1960s with the release of Letraset sheets containing Lorem Ipsum passages, and more recently with desktop publishing software like Aldus PageMaker including versions of Lorem Ipsum.</p>
  </div>
  <div class="signature" role="img" aria-label="Handwritten signature"></div>
  <div class="signer">YOUR NAME<small>Designation</small></div>
  <svg class="deco" viewBox="0 0 355 501" aria-hidden="true"><circle cx="300" cy="520" r="88" fill="var(--yellow)"/></svg>
</section>

<section class="piece card-front">
  <div class="brand">tallypal</div>
  <div class="person">ALAN REED<span>Director</span></div>
  <div class="rule"></div>
  <ul class="contacts">
    <li><span class="dot"></span>00-987-654-321</li>
    <li><span class="dot"></span>hello@tallypal.com</li>
    <li><span class="dot"></span>www.tallypal.com</li>
    <li><span class="dot"></span>48 Orchard Rd. Halden,</li>
  </ul>
</section>

<section class="piece card-back">
  <svg class="deco" viewBox="0 0 150 86" aria-hidden="true"><circle cx="150" cy="0" r="58" fill="var(--yellow)"/></svg>
  <div class="brand light">tallypal</div>
</section>

<section class="piece envelope-back">
  <div class="flap"></div>
  <div class="brand">tallypal</div>
</section>

<section class="piece envelope-front">
  <svg class="deco" viewBox="0 0 371 186" aria-hidden="true"><circle cx="371" cy="40" r="130" fill="var(--yellow)"/></svg>
  <div class="brand light">tallypal</div>
  <div class="contacts">00-987-654-321<br>hello@tallypal.com<br>www.tallypal.com<br>48 Orchard Rd. Halden, FL 32871</div>
  <div class="window"></div>
</section>

<section class="folder">
  <svg class="folder-flaps" viewBox="0 0 744 546" aria-hidden="true">
    <polygon points="66,0 0,40 0,420 66,466" fill="#fff"/>
    <polygon points="66,466 404,466 346,546 66,546" fill="#fff"/>
  </svg>
  <div class="cover-back">
    <div class="folder-contacts">
      <span><svg width="6" height="6" viewBox="0 0 10 10"><path d="M2 1l2 2-1 1.5c.8 1.5 1.8 2.5 3 3L7.5 6l2 2-1.5 1.5C4.5 9 1 5.5.5 2z" fill="#fff"/></svg>00-987-654-321</span>
      <span><svg width="7" height="5" viewBox="0 0 10 7"><rect x=".5" y=".5" width="9" height="6" fill="none" stroke="#fff"/><path d="M.5.5L5 4 9.5.5" fill="none" stroke="#fff"/></svg>hello@tallypal.com</span>
      <span><svg width="7" height="7" viewBox="0 0 10 10"><circle cx="5" cy="5" r="4.4" fill="none" stroke="#fff"/><ellipse cx="5" cy="5" rx="2" ry="4.4" fill="none" stroke="#fff"/><path d="M.6 5h8.8" stroke="#fff"/></svg>www.tallypal.com</span>
    </div>
  </div>
  <div class="cover-front">
    <svg class="deco" viewBox="0 0 340 466" aria-hidden="true"><circle cx="340" cy="60" r="230" fill="var(--yellow)"/></svg>
    <div class="brand">tallypal</div>
  </div>
</section>

<section class="piece slip">
  <svg class="deco" viewBox="0 0 308 146" aria-hidden="true"><circle cx="308" cy="0" r="80" fill="var(--yellow)"/></svg>
  <div class="brand">tallypal</div>
  <div class="contacts">00-987-654-321<br>hello@tallypal.com<br>www.tallypal.com<br>48 Orchard Rd. Halden, FL 32871</div>
  <div class="ribbon">With Compliments</div>
</section>

</body>
</html>
```